Halvorsen Partners Business Card

Halvorsen Partners Civil Construction
Marcus Halvorsen
CEO
727-518-6094
Marcus@HalvorsenSiteworks.example
www.HalvorsenSiteworks.example
Site Development
Utility Construction
Excavation
40876 County Lane 19
Bramble Cove, GA 30491

Target Market(s)

Construction and government

Industry/Entity Type

Business

Contact Information for Business Card

I want an unique design that make a statement

Number of Pages Required

1 page

Font styles to use

Colors

Designer to choose colors to be used in the design.

Requirements
Must have
• unique design, feel free to modify or change the color of my logo.
Nice to have
• extra design features like spot UV, foil accents, color edges, unique paper, or any thing that would make my card pop.
• I like the feel of the image that I attached

```html
<!DOCTYPE html>
<html lang="en">
<head>
<meta charset="utf-8">
<title>Halvorsen Partners Business Card</title>
<link rel="stylesheet" href="https://fonts.googleapis.com/css2?family=Marcellus&family=Arimo:ital,wght@0,400;0,700;1,400&display=swap">
<style>
  :root {
    --canvas-grey: #5f5f5f;
    --card-yellow: #edd335;
    --card-black: #000000;
    --ink-black: #0a0a0a;
    --paper-white: #ffffff;
    --edge-grey: #8a8a8a;
  }
  * { margin: 0; padding: 0; box-sizing: border-box; }
  html, body {
    width: 1040px;
    height: 1200px;
    overflow: hidden;
    background: var(--canvas-grey);
  }
  .sheet {
    position: relative;
    width: 1040px;
    height: 1200px;
  }
  .card {
    position: absolute;
    left: 31px;
    width: 984px;
    height: 563px;
  }
  .card--front {
    top: 31px;
    background: var(--card-yellow);
    border: 1px solid var(--edge-grey);
  }
  .card--back {
    top: 619px;
    background: var(--card-black);
  }
  .brand-square {
    position: absolute;
    background: var(--ink-black);
  }
  .card--front .brand-square {
    left: 406px;
    top: 72px;
    width: 172px;
    height: 172px;
  }
  .company-name {
    position: absolute;
    left: 0;
    right: 0;
    top: 330px;
    text-align: center;
    font-family: "Marcellus", "Optima", serif;
    font-size: 66px;
    font-weight: 400;
    line-height: 1;
    letter-spacing: 0;
    color: var(--ink-black);
    text-transform: uppercase;
    white-space: nowrap;
  }
  .company-trade {
    position: absolute;
    left: 0;
    right: 0;
    top: 408px;
    text-align: center;
    font-family: "Marcellus", "Optima", serif;
    font-size: 42px;
    line-height: 1;
    letter-spacing: 15px;
    padding-left: 15px;
    color: var(--paper-white);
    text-transform: uppercase;
    white-space: nowrap;
  }
  .divider {
    position: absolute;
    left: 155px;
    width: 675px;
    top: 475px;
    height: 1px;
    background: var(--ink-black);
  }
  .services {
    position: absolute;
    left: 0;
    right: 0;
    top: 496px;
    text-align: center;
    font-family: "Arimo", "Helvetica", sans-serif;
    font-size: 20px;
    line-height: 1;
    letter-spacing: 1.5px;
    color: var(--ink-black);
    text-transform: uppercase;
    white-space: nowrap;
  }
  .person {
    position: absolute;
    left: 62px;
    top: 52px;
    color: var(--paper-white);
    font-family: "Arimo", "Helvetica", sans-serif;
  }
  .person__name {
    font-size: 48px;
    font-weight: 700;
    letter-spacing: 3.5px;
    line-height: 1;
    text-transform: uppercase;
    white-space: nowrap;
  }
  .person__role {
    margin-top: 8px;
    font-size: 34px;
    font-style: italic;
    letter-spacing: 1.5px;
    line-height: 1;
  }
  .card--back .brand-square {
    left: 834px;
    top: 38px;
    width: 96px;
    height: 96px;
    background: var(--card-yellow);
  }
  .contact {
    position: absolute;
    right: 54px;
    top: 273px;
    text-align: right;
    font-family: "Arimo", "Helvetica", sans-serif;
    font-size: 28px;
    line-height: 39px;
    letter-spacing: 2px;
    color: var(--paper-white);
    text-transform: uppercase;
    font-style: normal;
    white-space: nowrap;
  }
  .contact__gap { height: 39px; }
</style>
</head>
<body>
  <main class="sheet">
    <section class="card card--front">
      <div class="brand-square"></div>
      <h1 class="company-name">Halvorsen Partners</h1>
      <p class="company-trade">Civil Construction</p>
      <div class="divider"></div>
      <p class="services">Site Development | Utility Construction | Excavation</p>
    </section>

    <section class="card card--back">
      <div class="person">
        <h2 class="person__name">Marcus Halvorsen</h2>
        <p class="person__role">CEO</p>
      </div>
      <div class="brand-square"></div>
      <address class="contact">
        <div>727-518-6094</div>
        <div>Marcus@HalvorsenSiteworks.example</div>
        <div class="contact__gap"></div>
        <div>40876 County Lane 19</div>
        <div>Bramble Cove, GA 30491</div>
        <div>www.HalvorsenSiteworks.example</div>
      </address>
    </section>
  </main>
</body>
</html>
```